www.brightlingua.net -- International Language school needs a Wordpress Design

NOTE: This is for a complete WordPress website with coding (Design/develop)

We are a small, private English language school in business for 15 years. Our students come from around the world to study English at our centre in Toronto, Canada. Most of our students are in their 20's and come to study English with us for periods of 1-6 months before returning home to complete their post-secondary education or pursue their careers.

We are looking for a talented web designer to redevelop our sadly outdated website (www.brightlingua.net) to bring a fresh look with vastly increased functionality and web traffic.

Target Market(s)

-20s and 30s; mostly upper-middle class, educated
-from non-English speaking countries, but often have some English background
-looking to improve their English (mostly speaking) skills at our school like ours and experience living in a new country (like exchange students)

Industry/Entity Type

Education

Font styles to use
Sans Serif

Requirements
Must have
• - page listing our programs
- page with our fees and starting dates
- application form
- page showing why BRIGHT (us)?
- page with accommodation options
* responsive design
Nice to have
• examples of other websites in our industry I like:

http://www.halvorsenlang.com/
http://www.pqlearning.com/en
http://en.rtz.ca/
http://www.marstowe-academy.ac.uk/

```html
<!DOCTYPE html>
<html lang="en">
<head>
<meta charset="utf-8">
<title>BRIGHT – International Language School</title>
<link href="https://fonts.googleapis.com/css2?family=Arvo:wght@400;700&family=Rokkitt:wght@300;400;700&family=Arimo:wght@400;700&display=swap" rel="stylesheet">
<style>
:root{
  --dark:#2b2b2b;
  --red:#c8381e;
  --red-light:#e2614a;
  --ink:#222222;
  --muted:#9a9a9a;
  --band:#ebebeb;
  --panel:#f1f1f1;
  --soft:#f8f8f8;
  --white:#ffffff;
  --rule:#d6d6d6;
}
*{margin:0;padding:0;box-sizing:border-box}
html,body{width:813px;height:1200px;overflow:hidden;background:var(--white)}
body{position:relative;font-family:"Arimo",sans-serif;color:var(--ink)}
.abs{position:absolute}

.topbar{left:102px;top:0;width:645px;height:30px;background:var(--dark)}
.topbar .social{left:76px;top:11px;display:flex;gap:7px}
.topbar .social span{width:7px;height:7px;border-radius:50%;background:#d0d0d0;display:block}
.topbar .tagline{right:12px;top:7px;font-size:5px;color:#cfcfcf;text-align:right;line-height:1.3}
.topbar .phone{display:block;color:var(--red-light);font-size:8px;font-family:"Rokkitt",serif}

.brand{left:184px;top:36px;width:60px;text-align:center}
.brand .dot{width:26px;height:26px;border-radius:50%;background:#3fa0d8;margin:0 auto 2px}
.brand .name{font-family:"Arvo",serif;font-weight:700;font-size:15px;color:var(--ink);letter-spacing:.5px}

.nav{left:334px;top:58px;display:flex;gap:7px;font-family:"Rokkitt",serif;font-size:6px;font-weight:700;color:var(--ink)}
.nav .active{color:var(--red)}

.hero{left:0;top:90px;width:813px;height:304px;background:linear-gradient(100deg,#b08a72 0%,#d9b59b 30%,#6e4a3a 50%,#c79a80 70%,#e8e2df 100%)}

.band{left:102px;top:394px;width:642px;height:78px;background:var(--band)}
.slide{left:178px;top:346px;width:228px;height:126px;background:var(--red);color:var(--white);padding:10px 22px}
.slide h1{font-family:"Rokkitt",serif;font-weight:300;font-size:42px;line-height:1;letter-spacing:1px}
.slide h2{font-family:"Rokkitt",serif;font-weight:400;font-size:15px;line-height:.9;margin-top:2px}
.slide p{font-family:"Rokkitt",serif;font-size:6.5px;line-height:1.5;margin-top:2px;opacity:.9}
.slide .arrows{margin-top:6px;font-size:10px;opacity:.6;letter-spacing:6px}
.welcome{left:418px;top:410px;font-family:"Arvo",serif}
.welcome h3{font-size:16px;font-weight:700;letter-spacing:.5px}
.welcome p{font-family:"Rokkitt",serif;font-size:15px;margin-top:6px}

.features{left:0;top:472px;width:813px;height:233px;background:var(--panel)}
.feature{top:492px;width:106px;text-align:center}
.feature .photo{width:72px;height:72px;border-radius:50%;border:2px solid var(--dark);margin:0 auto;background:linear-gradient(160deg,#8aa0b5,#c9a08a)}
.feature h4{font-family:"Arvo",serif;font-size:8px;font-weight:700;letter-spacing:.6px;margin-top:11px}
.feature p{font-size:5.4px;line-height:1.7;text-align:left;margin-top:6px;color:#333}
.btn{display:inline-block;background:var(--dark);color:var(--white);font-family:"Arvo",serif;font-size:5px;font-weight:700;padding:4px 10px;border-radius:1px}
.feature .btn{margin-top:27px}

.intro{left:102px;top:705px;width:645px;height:174px;background:var(--white)}
.section-title{font-family:"Arvo",serif;font-weight:700;font-size:8.5px;letter-spacing:.5px}
.program{top:775px;width:100px;text-align:center}
.program h5{font-family:"Arvo",serif;font-weight:700;font-size:13px;line-height:1}
.program h6{font-weight:400;font-size:8px;line-height:1.1;margin-top:1px}
.program .line{border-top:1px solid var(--rule);margin-top:5px}
.program p{font-size:4.6px;line-height:1.45;text-align:left;margin:5px 7px 0}
.program .more{display:block;font-family:"Arvo",serif;font-size:4.8px;font-weight:700;margin-top:11px}

.tips{left:102px;top:879px;width:645px;height:193px;background:var(--soft)}
.tips-title{left:176px;top:898px;font-family:"Arvo",serif;font-size:12px}
.tips-rule{left:176px;top:926px;width:470px;border-top:1px solid var(--rule)}
.lead{left:176px;top:952px;width:230px;font-family:"Arvo",serif;font-size:7.6px;font-weight:700;line-height:1.5}
.fine{left:176px;top:994px;width:228px;font-family:"Rokkitt",serif;font-size:5.6px;line-height:1.4;color:#b0b0b0}
.list{top:953px;font-family:"Rokkitt",serif}
.list h6{color:var(--red);font-size:5.2px;font-weight:700;letter-spacing:.3px}
.list ul{list-style:none;margin-top:6px}
.list li{font-size:5.8px;line-height:2.05;color:#555}
.list li::before{content:"•";color:var(--red);margin-right:3px}
.list .btn{margin-top:8px}
.calc{left:577px;top:954px;width:69px;height:86px;background:var(--red);color:var(--white);padding:24px 6px 0}
.calc svg{position:absolute;right:6px;top:7px}
.calc strong{display:block;font-family:"Arvo",serif;font-weight:400;font-size:7.4px;line-height:1.55;letter-spacing:.3px}
.calc .link{display:block;margin:6px -6px 0;background:#b22f17;font-size:6px;color:var(--red-light);font-family:"Rokkitt",serif;padding:4px 12px}

.footer-rule{left:106px;top:1074px;width:641px;height:4px;background:#3a3a3a}
.footer{left:106px;top:1078px;width:641px;height:122px;background:var(--panel)}
.footer-brand{left:186px;top:1090px;width:60px;text-align:center}
.footer-social{left:175px;top:1148px;display:flex;gap:2px}
.footer-social span{width:18px;height:18px;border-radius:50%;background:#6b6b6b;display:block}
.footer-list{top:1130px;list-style:none;font-family:"Rokkitt",serif;font-size:5.8px;color:#999;line-height:2.05}
.footer-list li::before{content:"•";color:var(--red);margin-right:4px}
</style>
</head>
<body>

<div class="abs topbar">
  <div class="abs social"><span></span><span></span><span></span><span></span><span></span></div>
  <div class="abs tagline">Lorem ipsum dolor sit amet conse ctetur adipisicingelit.<span class="phone">(800) 555 0148</span></div>
</div>

<div class="abs brand"><div class="dot"></div><div class="name">BRIGHT</div></div>

<nav class="abs nav">
  <span class="active">HOME</span><span>/</span><span>OUR SCHOOL</span><span>/</span><span>PROGRAMS</span><span>/</span><span>FEETSDATES</span><span>/</span><span>ACCOMODATION /</span><span>AFTER CLASS</span><span>/</span><span>AGENTS</span>
</nav>

<div class="abs hero" role="img" aria-label="Photo of a smiling group of young international students"></div>

<div class="abs band"></div>
<div class="abs slide">
  <h1>MAKE</h1>
  <h2>FRIENDS FROM AROUN<br>THE WORLD!</h2>
  <p>Lorem ipsum dolor sit amet, consectetur adipiscing elit, sed do eiusmod tempor sapiente delectus, ut aut reiciendis.</p>
  <div class="arrows">‹ ›</div>
</div>
<div class="abs welcome"><h3>WELCOME!</h3><p>Our School</p></div>

<div class="abs features"></div>
<div class="abs feature" style="left:178px">
  <div class="photo" role="img" aria-label="Photo of students on an outdoor trip"></div>
  <h4>ASK A QUESTION</h4>
  <p>Lorem ipsum dolor sit amet, consectetur adipiscing elit. Vivamus fringilla libero nec maximus ornare. Lorem ipsum dolor sit amet, consectetur</p>
  <span class="btn">MORE</span>
</div>
<div class="abs feature" style="left:300px">
  <div class="photo" role="img" aria-label="Photo of a smiling student"></div>
  <h4>GET A QUOTE</h4>
  <p>Lorem ipsum dolor sit amet, consectetur adipiscing elit. Vivamus fringilla libero nec maximus ornare. Lorem ipsum dolor sit amet, consectetur</p>
  <span class="btn">MORE</span>
</div>
<div class="abs feature" style="left:420px">
  <div class="photo" role="img" aria-label="Photo of a smiling teacher"></div>
  <h4>APPLY NOW</h4>
  <p>Lorem ipsum dolor sit amet, consectetur adipiscing elit. Vivamus fringilla libero nec maximus ornare. Lorem ipsum dolor sit amet, consectetur</p>
  <span class="btn" style="margin-top:20px">MORE</span>
</div>
<div class="abs feature" style="left:540px">
  <div class="photo" role="img" aria-label="Photo of a group of students"></div>
  <h4>NEWS</h4>
  <p>Lorem ipsum dolor sit amet, consectetur adipiscing elit. Vivamus fringilla libero nec maximus ornare. Lorem ipsum dolor sit amet, consectetur</p>
  <span class="btn">MORE</span>
</div>

<div class="abs intro"></div>
<div class="abs section-title" style="left:176px;top:736px">BRIEF INTRO TO SCHOOL</div>
<div class="abs program" style="left:180px"><h5>ADULT</h5><h6>ENGLISH PROGRAMS</h6><div class="line"></div><p>Lorem ipsum dolor sit amet, consectetur adipiscing elit. Vivamus fringilla libero nec maximus ornare. Proin nec est vitae mauris fermentum maximus a eget lectus.</p><span class="more">MORE</span></div>
<div class="abs program" style="left:301px"><h5>JUNIOR</h5><h6 style="font-size:7px">CAMPS PARENT<br>CHILD PROGRAM</h6><div class="line" style="margin-top:2px"></div><p>Lorem ipsum dolor sit amet, consectetur adipiscing elit. Vivamus fringilla libero nec maximus ornare. Proin nec est vitae mauris fermentum maximus a eget lectus.</p><span class="more">MORE</span></div>
<div class="abs program" style="left:422px"><h5>PATHWAY</h5><h6 style="font-size:7px">PROGRAM</h6><div class="line"></div><p>Lorem ipsum dolor sit amet, consectetur adipiscing elit. Vivamus fringilla libero nec maximus ornare. Proin nec est vitae mauris fermentum maximus a eget lectus.</p><span class="more">MORE</span></div>
<div class="abs program" style="left:542px"><h5>WORKING</h5><h6 style="font-size:7px">HOLIDAY PROGRAMS</h6><div class="line"></div><p>Lorem ipsum dolor sit amet, consectetur adipiscing elit. Vivamus fringilla libero nec maximus ornare. Proin nec est vitae mauris fermentum maximus a eget lectus.</p><span class="more">MORE</span></div>

<div class="abs tips"></div>
<div class="abs tips-title">Tips to Help You Prepare for Retirement:</div>
<div class="abs tips-rule"></div>
<p class="abs lead">Lorem ipsum dolor sit amet, consectetur adipisicing elit, sed do eiusmod tempor incididunt ut et dolore magna aliqua.</p>
<p class="abs fine">At vero eos et accusamus et iusto odio dignissimos ducimus qui blanditiis praesentium voluptatum deleniti atque corrupti quos dolores et quas molestias excepturi sint occaecati cupiditate non provident, similique sunt in culpa qui.</p>
<div class="abs list" style="left:417px">
  <h6>TEMPORIBUS AUTEM</h6>
  <ul><li>At vero eos et accusa</li><li>Ausro odio dignisois</li><li>Scimus qui blanditiis</li><li>Esentium voluptatum</li></ul>
  <span class="btn">MORE</span>
</div>
<div class="abs list" style="left:497px">
  <h6>ITAQUE EARUM RERUM</h6>
  <ul><li>Ero eos et accusamus</li><li>Austo odio dignisois</li><li>Scimus qui blanditiis</li><li>Esentium voluptatum</li></ul>
  <span class="btn">MORE</span>
</div>
<div class="abs calc">
  <svg width="22" height="22" viewBox="0 0 22 22" fill="none" stroke="#ffffff" stroke-width="1.4" aria-hidden="true">
    <rect x="2" y="1" width="11" height="16" rx="1"/>
    <line x1="4" y1="5" x2="11" y2="5"/>
    <path d="M5 9h1M8 9h1M5 12h1M8 12h1"/>
    <line x1="14" y1="20" x2="20" y2="12"/>
    <circle cx="15" cy="13" r="1.4"/><circle cx="19.5" cy="19" r="1.4"/>
  </svg>
  <strong>ROTH<br>RETIREMENT<br>CALCULATOR</strong>
  <span class="link">click here!</span>
</div>

<div class="abs footer-rule"></div>
<div class="abs footer"></div>
<div class="abs footer-brand"><div class="brand" style="position:static;width:auto"><div class="dot"></div><div class="name">BRIGHT</div></div></div>
<div class="abs footer-social"><span></span><span></span><span></span><span></span></div>
<ul class="abs footer-list" style="left:296px"><li>Lorem ipsum dolor sit amet</li><li>Consectetur adipiscing</li><li>Elit sed do eiusmod tempor</li><li>Encididunt ut labore</li></ul>
<ul class="abs footer-list" style="left:417px"><li>Asum dolor sit amet</li><li>Dectetur adipiscing</li><li>Elit sed do eiusmod</li><li>Acididunt ut labore</li></ul>
<ul class="abs footer-list" style="left:538px"><li>Dolor sit amet</li><li>Ensectetur adipiscing</li><li>Sed do eiusmod tempor</li><li>Encididunt ut labore</li></ul>

</body>
</html>
```